Welcome Center Signage/logo Design with Multicultural Relevance

We are looking to have a welcome signage/logo designed for our church lobby with either the word "welcome" or "Welcome to the Maplecrest Fellowship Church!"

This design must include our organizational logo (attached). It could (but does not need to) also include our church vision: "Our vision is to be a thriving diverse urban church sharing Christ's love and serving the needs of our local and global communities." The logo/signage will be printed on 4' x 6' stretch fabric.

This signage will then be hung up behind our welcome center...it will be one of the first things people see upon entering our building.

We are an urban multicultural church that has significant outreach into our local community, one that is quite culturally diverse. If you would like more information about our church, please visit www.maplecrestfellow.org.
Updates

Project Deadline Extended
Reason: We have committed to continue work with the designers on designs submitted over the last several days, and are scheduling the additional time needed to do so. Thank you!

Target Market(s)

Culturally (African American, Hispanic American, Asian American, European American) diverse millennials and iGens

Industry/Entity Type

Church

Font styles to use
Sans Serif

Requirements
Must have
• Our logo
Nice to have
• "Welcome" in many languages
Should not have
• I can't think of anything at the moment.

```html
<!DOCTYPE html>
<html lang="en">
<head>
<meta charset="utf-8">
<title>Welcome Sign – Maplecrest Fellowship Church</title>
<link rel="stylesheet" href="https://fonts.googleapis.com/css2?family=Arimo:wght@400;700&family=Noto+Sans+TC:wght@400&display=swap">
<style>
  :root {
    --sign-grey: #85827a;
    --ink-maroon: #5b2140;
    --ink-soft: #4a3a40;
    --mark-fill: #6e2a3f;
    --mark-text: #f2e6d0;
  }
  * { margin: 0; padding: 0; box-sizing: border-box; }
  html, body {
    width: 1200px;
    height: 750px;
    overflow: hidden;
    background: var(--sign-grey);
  }
  .welcome-sign {
    position: relative;
    width: 1200px;
    height: 750px;
    background: var(--sign-grey);
    font-family: "Arimo", Arial, sans-serif;
    text-align: center;
  }
  .church-mark {
    position: absolute;
    left: 400px;
    top: 32px;
    width: 400px;
    height: 400px;
  }
  .church-mark__name {
    font-family: "Arimo", Arial, sans-serif;
    font-weight: 700;
    font-size: 34px;
    fill: var(--mark-text);
  }
  .greeting {
    position: absolute;
    left: 0;
    width: 100%;
    color: var(--ink-maroon);
    font-weight: 700;
    letter-spacing: -0.5px;
  }
  .greeting--first { top: 500px; font-size: 56px; }
  .greeting--second { top: 598px; font-size: 56px; }
  .greeting--chinese {
    top: 672px;
    font-family: "Noto Sans TC", sans-serif;
    font-weight: 400;
    font-size: 44px;
    color: var(--ink-soft);
  }
</style>
</head>
<body>
  <main class="welcome-sign">
    <svg class="church-mark" viewBox="0 0 400 400" role="img" aria-label="Maplecrest Fellowship Church">
      <circle cx="200" cy="200" r="196" fill="var(--mark-fill)"/>
      <text class="church-mark__name" x="200" y="190" text-anchor="middle">Maplecrest</text>
      <text class="church-mark__name" x="200" y="232" text-anchor="middle">Fellowship Church</text>
    </svg>
    <p class="greeting greeting--first">Welcome! Bienvenido! Välkommen!</p>
    <p class="greeting greeting--second">Herzlich Willkommen!</p>
    <p class="greeting greeting--chinese" lang="zh-Hant">歡迎！</p>
  </main>
</body>
</html>
```